Business Card and Word .doc header and footer required

I need a business card designed for my cybersecurity consulting company. Also required, is a header and footer to be ued for my word documents.
Attached is the Logo design, font and rgb used.

Industry/Entity Type

Cyber Security Consulting

Contact Information for Business Card

Name, Phone, email, website

Colors
0054AA
0677BA
7BADD7
CADEEF
E8F1F8

Requirements
Must have
• Sleek, modern

```html
<!DOCTYPE html>
<html lang="en">
<head>
<meta charset="utf-8">
<title>Harrow Vale Consulting – Business Card</title>
<link rel="stylesheet" href="https://fonts.googleapis.com/css2?family=Montserrat:wght@400;500;600;700&display=swap">
<style>
  :root {
    --page-bg: #1c1c1e;
    --card-bg: #0a0a0b;
    --ink-white: #f2f4f6;
    --ink-silver: #c9ced4;
    --brand-blue: #0677ba;
    --brand-sky: #7badd7;
    --rule: #3a3d42;
  }
  * { box-sizing: border-box; margin: 0; padding: 0; }
  html, body {
    width: 1200px; height: 900px; overflow: hidden;
    background: var(--page-bg);
    font-family: "Montserrat", Arial, sans-serif;
  }
  .sheet {
    width: 1200px; height: 900px;
    display: flex; flex-direction: column; align-items: center; justify-content: center;
    gap: 50px;
  }
  .card {
    width: 630px; height: 360px;
    background: var(--card-bg);
    box-shadow: 0 18px 40px rgba(0,0,0,.55);
    position: relative;
  }

  /* Front */
  .card--front { display: flex; align-items: center; }
  .brand-block {
    width: 305px; height: 100%;
    display: flex; align-items: center; justify-content: center;
  }
  .divider {
    width: 1px; height: 210px; background: var(--rule);
  }
  .contact-block {
    flex: 1; padding-left: 34px;
    color: var(--ink-white);
  }
  .person-name {
    font-weight: 700; font-size: 22px; letter-spacing: 1px; text-transform: uppercase;
  }
  .person-role {
    font-weight: 500; font-size: 14px; letter-spacing: 1px; text-transform: uppercase;
    color: var(--brand-blue); margin-top: 2px;
  }
  .contact-list { list-style: none; margin-top: 20px; }
  .contact-list li {
    display: flex; align-items: center; gap: 10px;
    font-size: 15px; font-weight: 500; line-height: 26px;
  }
  .contact-list svg { width: 16px; height: 16px; flex: none; }
  .accent { color: var(--brand-blue); }
  .address {
    margin-top: 18px; font-size: 15px; font-weight: 500; line-height: 22px;
  }

  /* Brand lockup */
  .lockup {
    display: flex; align-items: center; gap: 12px;
  }
  .lockup-dot {
    width: 22px; height: 22px; border-radius: 50%; background: var(--brand-blue); flex: none;
  }
  .lockup-name {
    color: var(--ink-silver); font-weight: 700; font-size: 24px;
    letter-spacing: 1.5px; text-transform: uppercase; line-height: 1.2;
  }

  /* Back */
  .card--back { display: flex; align-items: center; justify-content: center; }
  .card--back .lockup-name { font-size: 30px; }
  .card--back .lockup-dot { width: 28px; height: 28px; }
</style>
</head>
<body>
<main class="sheet">

  <section class="card card--front" aria-label="Business card front">
    <div class="brand-block">
      <div class="lockup">
        <span class="lockup-dot"></span>
        <span class="lockup-name">Harrow Vale<br>Consulting</span>
      </div>
    </div>
    <div class="divider"></div>
    <div class="contact-block">
      <h1 class="person-name">Daniel Marsh</h1>
      <p class="person-role">Managing Director</p>
      <ul class="contact-list">
        <li>
          <svg viewBox="0 0 16 16" aria-hidden="true"><path d="M4 1.5l2.2 3-1.3 1.4a8 8 0 0 0 5.2 5.2l1.4-1.3 3 2.2-1.3 2.3C7.5 14.5 1.5 8.5 1.8 2.8z" fill="none" stroke="#0677ba" stroke-width="1.4" stroke-linejoin="round"/></svg>
          044-987 654 321
        </li>
        <li>
          <svg viewBox="0 0 16 16" aria-hidden="true"><rect x="1" y="3.5" width="14" height="9.5" fill="#0677ba"/><path d="M1 3.5l7 5.5 7-5.5" fill="none" stroke="#0a0a0b" stroke-width="1.2"/></svg>
          hello@harrowvale.com
        </li>
        <li>
          <svg viewBox="0 0 16 16" aria-hidden="true"><g fill="none" stroke="#0677ba" stroke-width="1.2"><circle cx="8" cy="8" r="6.5"/><ellipse cx="8" cy="8" rx="2.8" ry="6.5"/><path d="M1.5 8h13M2.5 4.8h11M2.5 11.2h11"/></g></svg>
          <span>www.<span class="accent">harrowvale</span>.com</span>
        </li>
      </ul>
      <p class="address">17, Meridian Road<br>20418, Northshire</p>
    </div>
  </section>

  <section class="card card--back" aria-label="Business card back">
    <div class="lockup">
      <span class="lockup-dot"></span>
      <span class="lockup-name">Harrow Vale<br>Consulting</span>
    </div>
  </section>

</main>
</body>
</html>
```